Vostra Capital Web Design

Vostra Capital Limited Shenzhen

This project is a 10 page launch website.
Our client is seeking a contemporary homepage design for a Holdings company. Once we are happy with the homepage design and select designer we will request a secondary page design.

Please see attached company LOGO for an idea of style, it incorporates the traditional Chinese furniture lattice work. The Coral Dune website is one of our clients favorite so we would like to see a similar homepage design to this website.

Use the websites below for reference purpose. The first two are Chinese and the second two are international. We would like to see elements of both but more focus on international design.

http://www.evergrande.com/http://www.orliqueholdings.example/pub/default.aspx http://www.coraldune.example/zh/resort_kelvanoru/
http://www.velde-studio.example
http://img-store-a1.picvault.example/originals/4f/a2/91/4fa291c03b7e55d1a86e20f9c4b713ee.jpg

Company Background
VOSTRA CAPITAL, located in Qianhai, China, is a new real-estate project operator, structuring urban-rural real-estate investment and development, and industrial fund investment. The company also invests in supply chain management and supporting infrastructures. To create new spaces and livable cities Vostra Capital develop win-win strategic partnerships with a number of institutions. Currently cooperating with Marlow East Fenbrook, China urban and rural integrated demonstration.

Target Market(s)

B2B property investment. Target market customers are senior level management/decision makers of large corporations. Focusing geographically on the domestic market first and expanding internationally in 2nd and 3rd years.

Industry/Entity Type

Investment

Requirements
Must have
• Since this is a new company, we would like to the website representing growth and power, E.g. like a growing tree.
Should not have
• Low-level vectors such as curency symbols, American dollar.

```html
<!DOCTYPE html>
<html lang="en">
<head>
<meta charset="utf-8">
<title>Vostra Capital — Home</title>
<link href="https://fonts.googleapis.com/css2?family=Cinzel:wght@400;600&family=Open+Sans:ital,wght@0,400;0,600;0,700;1,600;1,700&display=swap" rel="stylesheet">
<style>
:root{
  --page:#f8ece4;
  --panel:#e7e7e8;
  --ink:#4a4a4a;
  --dark:#1a100c;
  --gold:#c9a24a;
  --footer:#58585a;
  --rule:#b9b9b9;
  --white:#ffffff;
}
*{box-sizing:border-box;margin:0;padding:0}
html,body{width:1071px;height:1200px;overflow:hidden}
body{background:var(--page);font-family:"Open Sans",Arial,sans-serif;color:var(--ink);position:relative}
.backdrop{position:absolute;left:0;top:0;width:1071px;height:434px;
  background:linear-gradient(90deg,#3a4a66 0%,#8d8fa3 12%,#c9c6c8 15.2%,#c9c6c8 84.8%,#b8c0c4 86%,#6d7a82 100%)}
.site{position:absolute;left:163px;top:0;width:745px}
.hero{position:absolute;left:0;top:0;width:745px;height:408px;
  background:linear-gradient(180deg,#dfe9f5 0%,#a9c2dc 25%,#6d90b5 45%,#2f6fa8 60%,#5f8fa8 75%,#8b9a86 100%)}
.logo-tab{position:absolute;left:7px;top:0;width:153px;height:184px}
.logo-name{position:absolute;left:7px;top:108px;width:153px;text-align:center;
  font-family:"Cinzel",Georgia,serif;font-weight:600;font-size:13px;color:var(--gold);letter-spacing:.5px}
.logo-mark{position:absolute;left:62px;top:34px;width:44px;height:44px;border-radius:50%;background:var(--gold)}
.nav{position:absolute;left:168px;top:46px;width:577px;height:59px;background:var(--dark);
  display:flex;justify-content:flex-end;align-items:center;padding-right:36px;gap:0}
.nav a{color:var(--white);text-decoration:none;font-size:15px}
.nav span{color:var(--white);font-size:15px;margin:0 15px}
.arrow{position:absolute;top:288px}
.tagline{position:absolute;left:0;top:408px;width:745px;height:61px;background:var(--dark)}
.tagline h2{position:absolute;left:150px;top:14px;font-family:"Cinzel",Georgia,serif;font-weight:400;
  font-size:26px;color:var(--white);letter-spacing:1px}
.btn{display:block;position:absolute;background:linear-gradient(#e4e4e4,#9d9d9d);border:1px solid #777;
  border-radius:3px;color:#222;font-weight:600;text-align:center;text-decoration:none}
.tagline .btn{left:582px;top:19px;width:93px;height:24px;font-size:12px;line-height:22px}
.content{position:absolute;left:0;top:469px;width:745px;height:612px;background:var(--panel)}
.intro{position:absolute;left:21px;top:24px;width:479px}
.intro h1{font-size:16.5px;font-weight:700;color:#555;line-height:1.2}
.intro h3{font-size:11.5px;font-style:italic;font-weight:700;color:#555;margin-bottom:18px}
.intro p{font-size:13.2px;line-height:17px;text-align:justify;text-indent:65px;margin-bottom:17px;color:#555}
.programs{position:absolute;left:531px;top:16px;width:214px}
.programs .photo{width:214px;height:144px;background:linear-gradient(160deg,#b9d3e2,#6fa7c0 45%,#d6e0e4);position:relative}
.programs .label{position:absolute;right:0;bottom:7px;width:163px;height:39px;background:var(--dark);
  color:var(--white);font-style:italic;font-size:16px;text-align:right;padding:9px 6px 0 0}
.programs p{font-size:10.2px;font-style:italic;font-weight:700;line-height:13.5px;text-align:justify;margin-top:10px;color:#555}
.programs .btn{position:static;width:83px;height:22px;font-size:10px;line-height:20px;margin-top:10px}
.rule{position:absolute;left:21px;width:679px;height:2px;background:var(--rule)}
.tiles{position:absolute;left:21px;top:378px;display:flex;gap:20px}
.tile{width:221px}
.tile .photo{height:156px}
.tile p{height:39px;background:var(--dark);color:var(--white);font-size:10px;font-style:italic;font-weight:700;
  line-height:12px;padding:5px 8px}
.footer{position:absolute;left:0;top:1081px;width:1071px;height:109px;background:var(--footer);text-align:center}
.social{display:flex;justify-content:center;gap:22px;margin-top:26px;height:24px;align-items:center}
.social .dot{width:20px;height:20px;border-radius:50%;background:var(--white)}
.footer small{display:block;color:var(--white);font-size:11px;font-weight:700;margin-top:20px}
</style>
</head>
<body>
<div class="backdrop" role="img" aria-label="Night city traffic on the left and a river with moored boats on the right"></div>
<div class="site">
  <header class="hero" role="img" aria-label="Panorama of a coastal city skyline with a curving waterfront and green fields">
    <svg class="logo-tab" viewBox="0 0 153 184"><path d="M0 0H153V170L76.5 184L0 170Z" fill="#1a100c" stroke="#c9a24a" stroke-width="3"/></svg>
    <div class="logo-mark"></div>
    <div class="logo-name">VOSTRA CAPITAL</div>
    <nav class="nav">
      <a href="#">Home</a><span>|</span><a href="#">About</a><span>|</span><a href="#">Services</a><span>|</span><a href="#">Blog</a><span>|</span><a href="#">Contact</a>
    </nav>
    <svg class="arrow" style="left:34px" width="24" height="50" viewBox="0 0 24 50"><path d="M20 4L4 25L20 46" fill="none" stroke="#fff" stroke-width="4"/></svg>
    <svg class="arrow" style="left:690px" width="24" height="50" viewBox="0 0 24 50"><path d="M4 4L20 25L4 46" fill="none" stroke="#fff" stroke-width="4"/></svg>
  </header>
  <section class="tagline">
    <h2>Trusted To Build Together</h2>
    <a class="btn" href="#">contact us</a>
  </section>
  <main class="content">
    <article class="intro">
      <h1>Lorem ipsum dolor sit amet, consectetur adipisicing elit</h1>
      <h3>Lorem ipsum dolor sit amet, consectetur adipisicing elit</h3>
      <p>Sed ut perspiciatis, unde omnis iste natus error sit voluptatem accusantium doloremque laudantium, totam rem aperiam eaque ipsa, quae ab illo inventore veritatis et quasi architecto beatae vitae dicta sunt, explicabo.</p>
      <p>Nemo enim ipsam voluptatem, quia voluptas sit, aspernatur aut odit aut fugit, sed quia consequuntur magni dolores eos, qui ratione voluptatem sequi nesciunt, neque porro quisquam est, qui dolorem ipsum, quia dolor sit amet consectetur adipisci[ng] velit, sed quia non numquam [do] eius modi tempora inci[di]dunt, ut labore et dolore magnam aliquam quaerat voluptatem. Ut enim ad minima veniam, quis nostrum exercitationem ullam corporis suscipit laboriosam, nisi ut aliquid ex ea commodi consequatur? Quis autem vel eum iure reprehenderit, qui in ea voluptate velit esse, quam nihil molestiae consequatur, vel illum, qui dolorem eum fugiat, quo voluptas nulla pariatur?</p>
    </article>
    <aside class="programs">
      <div class="photo" role="img" aria-label="Aerial rendering of a waterfront development">
        <div class="label">Our Programs</div>
      </div>
      <p>Sed ut perspiciatis, unde omnis iste natus error sit voluptatem accusantium doloremque laudantium, totam rem aperiam eaque ipsa, quae ab illo inventore veritatis et quasi architecto beatae vitae dicta sunt, explicabo. Nemo enim ipsam voluptatem, quia voluptas sit, aspernatur aut odit aut fugit, sed quia consequuntur magni dolores eos, qui</p>
      <a class="btn" href="#">Read More</a>
    </aside>
    <div class="rule" style="top:356px"></div>
    <div class="tiles">
      <div class="tile">
        <div class="photo" role="img" aria-label="Group of business professionals" style="background:linear-gradient(180deg,#f2f2f2,#b9b4ae 60%,#3a3434)"></div>
        <p>Sed ut perspiciatis, unde omnis iste natus error sit voluptatem accusantium</p>
      </div>
      <div class="tile">
        <div class="photo" role="img" aria-label="Carved stone monument under a cloudy sky" style="background:linear-gradient(180deg,#5f6266,#8a8c8e 50%,#7a6b52 80%,#9a9488)"></div>
        <p>Sed ut perspiciatis, unde omnis iste natus error sit voluptatem accusantium</p>
      </div>
      <div class="tile">
        <div class="photo" role="img" aria-label="City lights reflected on a river at night" style="background:linear-gradient(180deg,#2c2f3a,#3d3a40 45%,#b07a3a 62%,#1e1c22)"></div>
        <p>Sed ut perspiciatis, unde omnis iste natus error sit voluptatem accusantium</p>
      </div>
    </div>
    <div class="rule" style="top:597px"></div>
  </main>
</div>
<footer class="footer">
  <div class="social">
    <svg width="24" height="17" viewBox="0 0 24 17" aria-label="Email"><rect x="1" y="1" width="22" height="15" rx="2" fill="#fff"/><path d="M2 2L12 10L22 2" fill="none" stroke="#58585a" stroke-width="2"/></svg>
    <span class="dot"></span><span class="dot"></span><span class="dot"></span>
  </div>
  <small>Copyright © 2013 All Right Reserved by www.vostracapital.example</small>
</footer>
</body>
</html>
```